New cookbook recipes app with New Technology Devices

App description:
Main features description that differentiates it from the current apps on the market:
Beautiful recipe cookbook app -> great look&feel and great UX;
Mise en Place Tab (Sort/Setup) -> Instead to have only the ingredients and the steps to cook Tab this new/different tab will help the cook to get all ingredients(raw or pre-cooked) organized and in order to be used on the recipe. This is a game changer in the cook learn-process.
Will change/present/show a different concept for measure/count quantities. Instead of display only the cups/pinch/time-to-cook/table-spoon etc (non-precision units), will have all these units converted in grams/pounds and cook internal temperatures.

Other features:
The app will work in all devices (phones, tablets, and desktops);
Good search tool by category or term filtration system;
No ads on the app (will be a subscription fee monetization method);
Inside the recipe the app will show the quantities in the usual way (spoons, pinches, and others) and new way (grams or lb);
Serving change capability (e.g. Serving for 2 persons can change to 4 people and the app will calculate the ingredients for that);
Pixolune and social media share capability;
If the user is logged in, the favorites will be enabled (user can save their fav recipes);
The app will allow recording videos and photos of the making process to share on social media.

Result expected:
I need a non-workable app, showing the app Design and Flow, to work on Tablets and Phones.

Target Market(s)

Cooks, average people looking for new technologies to cook

Font styles to use
Serif
Sans Serif

Requirements
Must have
• Great look and feel.
Serving change capability and unit conversion
Should not have
• Ads on the app

```html
<!DOCTYPE html>
<html lang="en">
<head>
<meta charset="utf-8">
<title>OVA – Recipe App Screens</title>
<link rel="stylesheet" href="https://fonts.googleapis.com/css2?family=IBM+Plex+Sans:wght@400;500;600;700&family=PT+Sans:wght@400&display=swap">
<style>
  :root {
    --stage: #a0a0a0;
    --screen: #f3f0f2;
    --wine: #72001f;
    --wine-deep: #5a0a22;
    --orange: #e8401c;
    --ink: #1c1c1c;
    --ink-soft: #333;
    --line: #b9b9b9;
    --white: #ffffff;
    --save-green: #3cc21a;
  }
  * { box-sizing: border-box; margin: 0; padding: 0; }
  html, body { width: 1200px; height: 709px; overflow: hidden; }
  body {
    background: var(--stage);
    font-family: "IBM Plex Sans", Arial, sans-serif;
    color: var(--ink);
    position: relative;
  }
  .screen {
    position: absolute;
    top: 61px;
    width: 324px;
    height: 575px;
    background: var(--screen);
    overflow: hidden;
  }
  .screen--login { left: 64px; }
  .screen--gallery { left: 429px; }
  .screen--analyzer { left: 804px; }

  /* Login */
  .login-hero {
    position: absolute; left: 0; top: 0; width: 100%; height: 204px;
    background: radial-gradient(circle at 70% 30%, #a8223a 0%, #7a1230 45%, var(--wine-deep) 100%);
  }
  .login-hero__title {
    position: absolute; left: 22px; top: 16px;
    color: var(--white); font-size: 17px; font-weight: 500;
  }
  .brand-name {
    position: absolute; left: 0; right: 0; top: 80px; text-align: center;
    color: var(--white); font-size: 46px; font-weight: 700; letter-spacing: 1px;
  }
  .field {
    position: absolute; left: 21px; width: 283px; height: 49px;
    background: var(--white); border: 1px solid var(--line);
    font-size: 14px; font-weight: 500; padding: 0 15px; line-height: 47px;
  }
  .field--user { top: 243px; }
  .field--pass { top: 309px; }
  .btn-primary {
    position: absolute; left: 21px; width: 283px; height: 55px;
    background: var(--orange); color: var(--white);
    font-size: 19px; font-weight: 700; text-align: center; line-height: 55px;
    letter-spacing: .5px;
  }
  .btn-primary--login { top: 382px; }
  .btn-register {
    position: absolute; left: 107px; top: 467px; width: 108px; height: 39px;
    border: 2px solid var(--line); background: var(--screen);
    font-size: 14px; text-align: center; line-height: 35px;
  }
  .forgot-link {
    position: absolute; left: 0; right: 0; top: 534px; text-align: center;
    font-size: 14px;
  }

  /* App bar */
  .app-bar {
    position: absolute; left: 0; top: 0; width: 100%; height: 45px;
    background: var(--wine); color: var(--white);
    display: flex; justify-content: space-between; align-items: center;
    padding: 0 20px;
  }
  .app-bar__brand { font-size: 17px; font-weight: 700; }
  .app-bar__section { font-size: 16px; font-weight: 500; letter-spacing: .3px; }

  /* Gallery */
  .recipe-grid {
    position: absolute; left: 11px; top: 56px;
    display: grid; grid-template-columns: 147px 147px; column-gap: 9px; row-gap: 8px;
  }
  .recipe-tile {
    position: relative; height: 119px; overflow: hidden;
  }
  .recipe-tile__photo { position: absolute; inset: 0; }
  .recipe-tile__label {
    position: absolute; left: 13px; bottom: 10px;
    color: var(--white); font-size: 12.5px; font-weight: 700; letter-spacing: .3px;
  }
  .save-badge { position: absolute; right: 6px; top: 7px; width: 30px; height: 30px; }
  .photo-burger { background: linear-gradient(160deg, #6b5a4a, #3a3430 60%, #24201d); }
  .photo-salad { background: linear-gradient(150deg, #d9a24a, #a2552a 50%, #3c5a2a); }
  .photo-curry { background: linear-gradient(160deg, #2c2c2a, #c86a2c 45%, #e08a3c 70%, #3a3a34); }
  .photo-squash { background: linear-gradient(150deg, #3a3d40, #c86a22 50%, #2a2d30); }
  .photo-eggplant { background: linear-gradient(160deg, #8a8f94, #4a2f2a 55%, #2a1e1c); }
  .photo-pasta { background: linear-gradient(160deg, #8a8a88, #c0452a 50%, #5a5a58); }
  .photo-fries { background: linear-gradient(160deg, #1e1c1a, #b0782e 50%, #2a2420); }
  .photo-pastry { background: linear-gradient(160deg, #a8743e, #d8a25a 50%, #6e4a2a); }

  /* Analyzer */
  .section-label {
    position: absolute; left: 21px; top: 73px;
    font-size: 15.5px; font-weight: 700; letter-spacing: .3px; color: var(--ink-soft);
  }
  .ingredients-box {
    position: absolute; left: 21px; top: 105px; width: 283px; height: 267px;
    background: var(--white); border: 1px solid var(--line);
    padding: 16px 16px; font-family: "PT Sans", Arial, sans-serif; font-size: 12.5px;
    line-height: 24px; color: var(--ink-soft);
  }
  .servings-select {
    position: absolute; left: 21px; top: 390px; width: 283px; height: 55px;
    background: var(--white); border: 1px solid var(--line);
    display: flex; justify-content: space-between; align-items: center; padding: 0 17px;
    font-size: 14px; font-weight: 700; letter-spacing: .3px; color: var(--ink-soft);
  }
  .btn-primary--analyze { top: 473px; font-size: 18px; }
</style>
</head>
<body>

<section class="screen screen--login" aria-label="Login screen">
  <div class="login-hero" role="img" aria-label="Grilled skewers on a dark plate under a wine-red tint">
    <p class="login-hero__title">LOGIN</p>
    <p class="brand-name">OVA</p>
  </div>
  <div class="field field--user">USER NAME</div>
  <div class="field field--pass">PASSWORD</div>
  <div class="btn-primary btn-primary--login">LOGIN</div>
  <div class="btn-register">REGISTER</div>
  <p class="forgot-link">FORGOT PASSWORD?</p>
</section>

<section class="screen screen--gallery" aria-label="Recipe gallery screen">
  <header class="app-bar"><span class="app-bar__brand">OVA</span></header>
  <div class="recipe-grid">
    <div class="recipe-tile"><div class="recipe-tile__photo photo-burger" role="img" aria-label="Burger ingredients with sauces"></div>
      <svg class="save-badge" viewBox="0 0 30 30"><circle cx="15" cy="15" r="15" fill="var(--save-green)"/><path d="M9 9h10l3 3v9H9z" fill="#fff"/><rect x="12" y="9" width="6" height="4" fill="var(--save-green)"/><rect x="11.5" y="16" width="7" height="4" fill="var(--save-green)"/></svg>
      <span class="recipe-tile__label">LOREM IPSUM</span></div>
    <div class="recipe-tile"><div class="recipe-tile__photo photo-salad" role="img" aria-label="Pasta salad with vegetables"></div>
      <svg class="save-badge" viewBox="0 0 30 30"><circle cx="15" cy="15" r="15" fill="var(--save-green)"/><path d="M9 9h10l3 3v9H9z" fill="#fff"/><rect x="12" y="9" width="6" height="4" fill="var(--save-green)"/><rect x="11.5" y="16" width="7" height="4" fill="var(--save-green)"/></svg>
      <span class="recipe-tile__label">LOREM IPSUM</span></div>
    <div class="recipe-tile"><div class="recipe-tile__photo photo-curry" role="img" aria-label="Curry in a pan with herbs"></div>
      <svg class="save-badge" viewBox="0 0 30 30"><circle cx="15" cy="15" r="15" fill="var(--save-green)"/><path d="M9 9h10l3 3v9H9z" fill="#fff"/><rect x="12" y="9" width="6" height="4" fill="var(--save-green)"/><rect x="11.5" y="16" width="7" height="4" fill="var(--save-green)"/></svg>
      <span class="recipe-tile__label">LOREM IPSUM</span></div>
    <div class="recipe-tile"><div class="recipe-tile__photo photo-squash" role="img" aria-label="Stuffed roasted squash halves"></div>
      <svg class="save-badge" viewBox="0 0 30 30"><circle cx="15" cy="15" r="15" fill="var(--save-green)"/><path d="M9 9h10l3 3v9H9z" fill="#fff"/><rect x="12" y="9" width="6" height="4" fill="var(--save-green)"/><rect x="11.5" y="16" width="7" height="4" fill="var(--save-green)"/></svg>
      <span class="recipe-tile__label">LOREM IPSUM</span></div>
    <div class="recipe-tile"><div class="recipe-tile__photo photo-eggplant" role="img" aria-label="Grilled eggplant with pomegranate"></div>
      <svg class="save-badge" viewBox="0 0 30 30"><circle cx="15" cy="15" r="15" fill="var(--save-green)"/><path d="M9 9h10l3 3v9H9z" fill="#fff"/><rect x="12" y="9" width="6" height="4" fill="var(--save-green)"/><rect x="11.5" y="16" width="7" height="4" fill="var(--save-green)"/></svg>
      <span class="recipe-tile__label">LOREM IPSUM</span></div>
    <div class="recipe-tile"><div class="recipe-tile__photo photo-pasta" role="img" aria-label="Spaghetti with tomato sauce and basil"></div>
      <svg class="save-badge" viewBox="0 0 30 30"><circle cx="15" cy="15" r="15" fill="var(--save-green)"/><path d="M9 9h10l3 3v9H9z" fill="#fff"/><rect x="12" y="9" width="6" height="4" fill="var(--save-green)"/><rect x="11.5" y="16" width="7" height="4" fill="var(--save-green)"/></svg>
      <span class="recipe-tile__label">LOREM IPSUM</span></div>
    <div class="recipe-tile"><div class="recipe-tile__photo photo-fries" role="img" aria-label="Loaded fries with sauce"></div>
      <svg class="save-badge" viewBox="0 0 30 30"><circle cx="15" cy="15" r="15" fill="var(--save-green)"/><path d="M9 9h10l3 3v9H9z" fill="#fff"/><rect x="12" y="9" width="6" height="4" fill="var(--save-green)"/><rect x="11.5" y="16" width="7" height="4" fill="var(--save-green)"/></svg>
      <span class="recipe-tile__label">LOREM IPSUM</span></div>
    <div class="recipe-tile"><div class="recipe-tile__photo photo-pastry" role="img" aria-label="Baked empanadas"></div>
      <svg class="save-badge" viewBox="0 0 30 30"><circle cx="15" cy="15" r="15" fill="var(--save-green)"/><path d="M9 9h10l3 3v9H9z" fill="#fff"/><rect x="12" y="9" width="6" height="4" fill="var(--save-green)"/><rect x="11.5" y="16" width="7" height="4" fill="var(--save-green)"/></svg>
      <span class="recipe-tile__label">LOREM IPSUM</span></div>
  </div>
</section>

<section class="screen screen--analyzer" aria-label="Recipe analyzer screen">
  <header class="app-bar"><span class="app-bar__brand">OVA</span><span class="app-bar__section">RECIPE ANALYZER</span></header>
  <p class="section-label">INGREDIENTS</p>
  <div class="ingredients-box">
    <p>1/4 of onion, cubed</p>
    <p>1/2 tablespoon of butter</p>
  </div>
  <div class="servings-select">
    <span>SERVINGS: 1</span>
    <svg width="16" height="10" viewBox="0 0 16 10" aria-hidden="true"><path d="M0 0h16L8 9z" fill="var(--ink-soft)"/></svg>
  </div>
  <div class="btn-primary btn-primary--analyze">ANALYZE RECIPE</div>
</section>

</body>
</html>
```